Enhance the web site presence of Kolrith Global Limited

Upgrade the current web site www.kolrithpanel.com to share with the audience our current plan and future developments of our company. I have created a worksheet which shows all the pages that I like to have. The home page in English, Japanese and Chinese is hyperlinked to the various pages. Under the product, we should allow the user to select "single sided PCB or double sided PCB". The translation of the contents of the pages with Japanese is not complete but the English and Chinese are complete. You can download the briefing and photos in the dropbox files below;

https://www.sharelocker.net/sh/xk4trw92mpd3ab1/BBQm_Lp841zzPq2Rw7KtYnHjEa?dl=0

Target Market(s)

Electronic companies

Industry/Entity Type

Electronic

Coding

Coded - Design and coding required

Number of Pages Required

5+ page

Font styles to use
Sans Serif

Colors
00a990
0353a1
33b8a4

Requirements
Must have
• Get a sense of confidence on our company's integrity and capability to deliver the highest quality PCBs with the most competitive prices and best services. A sense of elegance is essential as we DON'T treat profits as the number one goal. Our number goal is to do the RIGHT things right. Having a mixture of our company photos will be appropriate.

```html
<!DOCTYPE html>
<html lang="en">
<head>
<meta charset="utf-8">
<title>Kolrith Global Limited — Home</title>
<link href="https://fonts.googleapis.com/css2?family=Roboto:wght@300;400;500;700;900&display=swap" rel="stylesheet">
<style>
  :root {
    --teal: #00a990;
    --teal-light: #33b8a4;
    --blue: #0353a1;
    --dark: #1c1c1c;
    --footer: #2f2f2f;
    --footer-deep: #222;
    --text: #555;
    --paper: #f5f6f6;
    --white: #fff;
  }
  * { margin: 0; padding: 0; box-sizing: border-box; }
  html, body { width: 670px; height: 1200px; overflow: hidden; }
  body { position: relative; font-family: "Roboto", Arial, sans-serif; background: var(--white); color: var(--text); }
  .abs { position: absolute; }

  /* hero */
  .hero-photo { left: 0; top: 0; width: 670px; height: 357px;
    background: radial-gradient(ellipse at 50% 40%, #2f5a6a 0%, #14303a 45%, #070d10 100%); }
  .topbar { left: 90px; top: 0; width: 490px; height: 22px; display: flex; align-items: center; gap: 8px; color: var(--white); font-size: 6.6px; }
  .topbar .item { display: flex; align-items: center; gap: 4px; margin-right: 4px; }
  .icon-circle { width: 12px; height: 12px; border: 1px solid var(--white); border-radius: 50%; display: flex; align-items: center; justify-content: center; }
  .lang { left: 524px; top: 5px; width: 56px; height: 13px; background: var(--teal); color: var(--white); font-size: 5.4px; display: flex; align-items: center; justify-content: center; gap: 4px; }
  .lang .flag { width: 11px; height: 7px; background: #2f4fa0; border: 1px solid #e24; }
  .nav { left: 90px; top: 22px; width: 489px; height: 36px; background: var(--white); display: flex; align-items: center; }
  .brand { margin-left: 8px; display: flex; align-items: center; gap: 5px; font-weight: 700; font-size: 15px; color: var(--dark); width: 150px; }
  .brand .mark { width: 9px; height: 9px; background: var(--teal); }
  .menu { display: flex; gap: 10px; font-size: 6.4px; color: #444; margin-left: 10px; }
  .menu .active { color: var(--teal); position: relative; }
  .menu .active::after { content: ""; position: absolute; left: 0; right: 0; top: 10px; height: 1px; background: var(--teal); }
  .login { left: 534px; top: 22px; width: 45px; height: 36px; background: var(--teal); color: var(--white); font-size: 6.4px; display: flex; align-items: center; justify-content: center; }
  .hero-title { left: 0; width: 670px; text-align: center; color: var(--white); font-weight: 700; }
  .hero-title.small { top: 149px; font-size: 19px; letter-spacing: .2px; }
  .hero-title.big { top: 170px; font-size: 35px; letter-spacing: .5px; }
  .read-more { left: 298px; top: 219px; width: 74px; height: 27px; background: var(--white); color: var(--teal); font-size: 6.4px; display: flex; align-items: center; justify-content: center; gap: 5px; }
  .arrow-side { top: 177px; }

  /* features */
  .feature { top: 312px; width: 245px; height: 88px; color: var(--white); display: flex; padding: 22px 0 0 22px; gap: 20px; }
  .feature.single { left: 90px; background: var(--teal-light); }
  .feature.double { left: 335px; background: var(--teal); }
  .feature h3 { font-weight: 400; font-size: 10px; margin: 0 0 6px; }
  .feature p { font-size: 6px; line-height: 1.5; width: 140px; font-weight: 300; }

  /* welcome */
  .plant-photo { left: 0; top: 425px; width: 336px; height: 186px; background: linear-gradient(135deg, #cfd3d0 0%, #8aa293 45%, #3f8a4b 75%, #6c7068 100%); }
  .slide-btns { left: 276px; top: 578px; display: flex; gap: 1px; }
  .slide-btns span { width: 27px; height: 27px; background: var(--white); display: flex; align-items: center; justify-content: center; }
  .welcome { left: 336px; top: 425px; width: 334px; height: 186px; background: var(--paper); padding: 23px 20px 0 18px; }
  .welcome h2 { color: var(--teal); font-size: 10px; font-weight: 700; margin-bottom: 12px; }
  .welcome p { font-size: 6px; line-height: 1.55; margin-bottom: 8px; color: #666; }

  /* contact */
  .contact { left: 0; top: 635px; width: 670px; height: 251px; background: linear-gradient(160deg, #28b9a3, #10a58d 55%, #07997f); }
  .section-title { left: 0; width: 670px; text-align: center; font-weight: 700; font-size: 14px; }
  .divider { left: 317px; width: 36px; height: 4px; }
  .field { left: 212px; width: 246px; border-bottom: 1px solid rgba(255,255,255,.75); color: var(--white); font-size: 6.2px; font-weight: 500; padding-bottom: 6px; }
  .submit { left: 305px; top: 834px; width: 60px; height: 22px; border: 1px solid var(--white); color: var(--white); font-size: 6.2px; display: flex; align-items: center; justify-content: center; }

  /* customers */
  .customers { left: 90px; top: 967px; width: 490px; display: flex; justify-content: space-between; align-items: center; font-weight: 900; font-size: 15px; }
  .pager { left: 320px; top: 1011px; display: flex; gap: 2px; }
  .pager span { width: 14px; height: 14px; background: #e6e6e6; display: flex; align-items: center; justify-content: center; }

  /* footer */
  .footer { left: 0; top: 1067px; width: 670px; height: 133px; background: var(--footer); }
  .info-bar { left: 88px; top: 1047px; width: 490px; height: 40px; background: var(--teal); display: flex; color: var(--white); font-size: 6px; line-height: 1.45; }
  .info-bar .cell { flex: 1; display: flex; align-items: center; gap: 12px; padding-left: 16px; border-right: 1px solid rgba(255,255,255,.35); margin: 6px 0; }
  .info-bar .cell:last-child { border-right: 0; }
  .footer-brand { left: 0; top: 1104px; width: 670px; text-align: center; color: #bbb; font-weight: 700; font-size: 14px; }
  .footer-nav { left: 208px; top: 1139px; width: 255px; height: 16px; border-top: 1px solid #666; border-bottom: 1px solid #666; display: flex; justify-content: space-between; align-items: center; color: #bbb; font-size: 5.4px; letter-spacing: .3px; }
  .copyright { left: 0; top: 1168px; width: 670px; height: 32px; background: var(--footer-deep); color: #aaa; font-size: 5.2px; letter-spacing: .3px; display: flex; align-items: center; justify-content: center; }
</style>
</head>
<body>

<div class="abs hero-photo" role="img" aria-label="Close-up photo of a dark printed circuit board"></div>

<div class="abs topbar">
  <span class="item"><span class="icon-circle"><svg width="6" height="6" viewBox="0 0 10 10"><path d="M2 1l2 2-1 1.5c.8 1.5 1.5 2.2 3 3L7.5 6l2 2-1.5 1.5C4 9 1 6 .5 2.5z" fill="#fff"/></svg></span>(852) 5550 2146</span>
  <span class="item"><span class="icon-circle"><svg width="6" height="5" viewBox="0 0 10 8"><rect x=".5" y=".5" width="9" height="7" fill="none" stroke="#fff"/><path d="M.5.5L5 4.5 9.5.5" fill="none" stroke="#fff"/></svg></span>SALES@KOLRITHPANEL.COM</span>
</div>
<div class="abs lang"><span class="flag"></span>ENGLISH<svg width="5" height="4" viewBox="0 0 10 6"><path d="M1 1l4 4 4-4" stroke="#fff" stroke-width="2" fill="none"/></svg></div>

<nav class="abs nav">
  <div class="brand"><span class="mark"></span>Kolrith</div>
  <div class="menu">
    <span class="active">HOME</span><span>PRODUCTS</span><span>OUT FACILITIES</span><span>CUSTOMERS</span><span>NEWS</span><span>QUOTES</span><span>CONTACT US</span>
  </div>
</nav>
<div class="abs login">LOG IN</div>

<svg class="abs arrow-side" style="left:10px" width="16" height="8" viewBox="0 0 16 8"><path d="M15 4H1M4 1L1 4l3 3" stroke="#00a990" stroke-width="1.3" fill="none"/></svg>
<svg class="abs arrow-side" style="left:644px" width="16" height="8" viewBox="0 0 16 8"><path d="M1 4h14M12 1l3 3-3 3" stroke="#00a990" stroke-width="1.3" fill="none"/></svg>

<div class="abs hero-title small">OUR PCB BUSINESS IS COMMITTED TO</div>
<div class="abs hero-title big">EXCELLENCE</div>
<div class="abs read-more">READ MORE <svg width="6" height="6" viewBox="0 0 10 10"><circle cx="5" cy="5" r="5" fill="#00a990"/><path d="M4 3l2 2-2 2" stroke="#fff" stroke-width="1.4" fill="none"/></svg></div>

<section class="abs feature single">
  <svg width="44" height="44" viewBox="0 0 44 44" fill="none" stroke="#fff" stroke-width="1.6"><rect x="15" y="15" width="14" height="14" rx="2" fill="#fff"/><path d="M19 15V8M25 15V5M29 19h7M29 25h9M25 29v8M19 29v5M15 25H8M15 19H5"/><circle cx="19" cy="6" r="2"/><circle cx="25" cy="3" r="2"/><circle cx="38" cy="19" r="2"/><circle cx="40" cy="25" r="2"/><circle cx="25" cy="39" r="2"/><circle cx="19" cy="36" r="2"/><circle cx="6" cy="25" r="2"/><circle cx="3" cy="19" r="2"/></svg>
  <div><h3>SINGLE SIDED PCB</h3><p>We are offering single layered circuit boards through our own production facility in China for customers in the following industries</p></div>
</section>
<section class="abs feature double">
  <svg width="44" height="44" viewBox="0 0 44 44" fill="none" stroke="#fff" stroke-width="1.6"><rect x="15" y="15" width="14" height="14" rx="2" fill="#fff"/><path d="M19 15V8M25 15V5M29 19h7M29 25h9M25 29v8M19 29v5M15 25H8M15 19H5"/><circle cx="19" cy="6" r="2"/><circle cx="25" cy="3" r="2"/><circle cx="38" cy="19" r="2"/><circle cx="40" cy="25" r="2"/><circle cx="25" cy="39" r="2"/><circle cx="19" cy="36" r="2"/><circle cx="6" cy="25" r="2"/><circle cx="3" cy="19" r="2"/></svg>
  <div><h3>DOUBLE SIDED PCB</h3><p>We are offering two layered and multi-layered circuit boards for our customers through our strategically approved printed circuit boards.</p></div>
</section>

<div class="abs plant-photo" role="img" aria-label="Photo of stacked green circuit boards beside production machinery"></div>
<div class="abs slide-btns">
  <span><svg width="7" height="9" viewBox="0 0 7 10"><path d="M5.5 1L1.5 5l4 4" stroke="#00a990" stroke-width="2" fill="none"/></svg></span>
  <span><svg width="7" height="9" viewBox="0 0 7 10"><path d="M1.5 1l4 4-4 4" stroke="#00a990" stroke-width="2" fill="none"/></svg></span>
</div>
<section class="abs welcome">
  <h2>Welcome to Kolrith Global Limited</h2>
  <p>Established in 2007, Kolrith Global Limited (Kolrith) is a Hong Kong company specializing in single and double sized printed circuit boards. Its manufacturing facility is located in a self-owned facility in Tangxia, Dongguan of China which is 50 minutes from Hong Kong.</p>
  <p>Our mission is to become a premium low costs PCB supplier that fully embraces human, social and environmental responsibilities.</p>
  <p>Through our insatiable drive to maximize efficiency, Kolrith is becoming a highly efficient PCB factory with a capacity of 140,000 square meter a month. PCB is our business and it is through continued automation and innovation that will drive our growth in the next 10 years.</p>
</section>

<section class="abs contact" role="img" aria-label="Factory floor photo under a teal tint"></section>
<div class="abs section-title" style="top:656px;color:#fff">CONTACT US</div>
<svg class="abs divider" style="top:678px" viewBox="0 0 36 4"><line x1="3" y1="2" x2="33" y2="2" stroke="#fff"/><circle cx="2" cy="2" r="1.5" fill="none" stroke="#fff"/><circle cx="34" cy="2" r="1.5" fill="none" stroke="#fff"/></svg>
<div class="abs field" style="top:711px">NAME</div>
<div class="abs field" style="top:737px">EMAIL</div>
<div class="abs field" style="top:761px">COMPANY NAME</div>
<div class="abs field" style="top:798px">COMMENTS</div>
<div class="abs submit">SUBMIT</div>

<div class="abs section-title" style="top:909px;color:var(--teal)">OUR CUSTOMERS</div>
<svg class="abs divider" style="top:931px" viewBox="0 0 36 4"><line x1="3" y1="2" x2="33" y2="2" stroke="#00a990"/><circle cx="2" cy="2" r="1.5" fill="none" stroke="#00a990"/><circle cx="34" cy="2" r="1.5" fill="none" stroke="#00a990"/></svg>
<div class="abs customers">
  <span style="color:#e2261c">VARNO</span>
  <span style="color:#1d6fb8">QUELLA</span>
  <span style="color:#1d8fd0">TIRMA</span>
  <span style="color:#e2261c">ZOD</span>
  <span style="color:#d7161e">HOLVEN</span>
  <span style="color:#d7161e">MERVIK</span>
</div>
<div class="abs pager">
  <span><svg width="5" height="6" viewBox="0 0 7 10"><path d="M5.5 1L1.5 5l4 4" stroke="#333" stroke-width="2" fill="none"/></svg></span>
  <span><svg width="5" height="6" viewBox="0 0 7 10"><path d="M1.5 1l4 4-4 4" stroke="#333" stroke-width="2" fill="none"/></svg></span>
</div>

<footer class="abs footer"></footer>
<div class="abs info-bar">
  <div class="cell"><span class="icon-circle" style="width:16px;height:16px"><svg width="6" height="8" viewBox="0 0 10 14"><path d="M5 13S1 8 1 5a4 4 0 018 0c0 3-4 8-4 8z" fill="#fff"/><circle cx="5" cy="5" r="1.5" fill="#00a990"/></svg></span><span>12/F Marlow Tower 88 Orchid Road<br>Harbour Bay, HONG KONG</span></div>
  <div class="cell"><span class="icon-circle" style="width:16px;height:16px"><svg width="5" height="8" viewBox="0 0 6 10"><rect x=".5" y=".5" width="5" height="9" rx="1" fill="none" stroke="#fff"/></svg></span><span>(852)55502146<br>(852)55508391</span></div>
  <div class="cell"><span class="icon-circle" style="width:16px;height:16px"><svg width="7" height="5" viewBox="0 0 10 7"><rect width="10" height="7" fill="#fff"/><path d="M0 0l5 4 5-4" stroke="#00a990" fill="none"/></svg></span><span>Sales@kolrithpanel.com<br>info@kolrithpanel.com</span></div>
</div>
<div class="abs footer-brand">Kolrith</div>
<div class="abs footer-nav"><span>HOME</span><span>PRODUCTS</span><span>OUT FACILITIES</span><span>CUSTOMERS</span><span>NEWS</span><span>QUOTES</span><span>CONTACT US</span></div>
<div class="abs copyright">COPYRIGHT © 2018, KOLRITH GLOBAL LIMITED. ALL RIGHTS RESERVED</div>

</body>
</html>
```